Mental Health care Company in Washington DC

We are a new mental health care services provider in Washington DC. Please look at these sites.
https://quarrystonewellbeingpartners.com
https://www.quietharborllc.com
https://fernvale-nb.org/
https://www.truepathnb.com
https://www.willowmeadnb.com

```html
<!DOCTYPE html>
<html lang="en">
<head>
<meta charset="utf-8">
<title>Vela Health Services</title>
<link rel="stylesheet" href="https://fonts.googleapis.com/css2?family=Montserrat:wght@500;600;700;800&family=Open+Sans:wght@400;600;700&family=Oswald:wght@500&family=Roboto:wght@500&display=swap">
<style>
:root{
  --orange:#f5a25d;
  --teal:#a8dde0;
  --teal-text:#8fd2d7;
  --hero-bg:#e6f8fa;
  --cream:#fdf3e3;
  --services-bg:#c9d7e0;
  --ink:#111;
  --muted:#9aa3a8;
  --white:#fff;
  --footer:#0b0b0b;
}
*{box-sizing:border-box;margin:0;padding:0}
html,body{width:1200px;height:4409px;overflow:hidden}
body{position:relative;background:var(--white);font-family:"Open Sans",sans-serif;color:var(--ink)}
section,header,footer{position:absolute;left:0;width:1200px}
.abs{position:absolute}
.photo{position:absolute;background:linear-gradient(160deg,#d9d4cc,#a9a198 60%,#7d7770)}
h1,h2{font-family:"Montserrat",sans-serif}
.btn{position:absolute;display:flex;align-items:center;justify-content:center;font-size:12px;font-weight:600;border-radius:4px}
.btn-orange{background:var(--orange);color:var(--white)}
.tagline{position:absolute;display:flex;align-items:center;gap:10px;font-size:16px}
.plus{width:24px;height:24px}

/* header */
.site-header{top:0;height:70px;background:var(--white)}
.brand{left:62px;top:12px;font-family:"Open Sans",sans-serif;font-size:28px;font-weight:600;color:#3a3a3a}
.nav{position:absolute;top:25px;left:0;font-size:12.5px;font-weight:600}
.nav a{position:absolute;color:var(--ink);text-decoration:none;white-space:nowrap}
.header-cta{left:966px;top:12px;width:173px;height:44px}

/* hero */
.hero{top:70px;height:644px;background:var(--hero-bg);overflow:hidden}
.hero .cream{left:620px;top:16px;width:580px;height:628px;background:var(--cream)}
.hero .teal-block{left:724px;top:233px;width:415px;height:394px;background:var(--teal)}
.hero .photo{left:678px;top:53px;width:406px;height:533px;border-radius:120px 0 0 0;background:linear-gradient(160deg,#e8ecea,#b49b7c 55%,#e39a3d)}
.hero h1{position:absolute;left:62px;top:114px;font-size:42px;line-height:47px;font-weight:800;width:520px}
.hero-lead{position:absolute;left:62px;top:276px;width:420px;font-size:13px;line-height:19.5px;color:var(--muted)}
.hero .btn-teal{left:62px;top:355px;width:200px;height:41px;background:var(--teal);color:var(--white)}
.hero .btn-outline{left:282px;top:355px;width:138px;height:41px;border:1.5px solid var(--orange);color:var(--orange);background:transparent}
.stat{position:absolute;top:460px}
.stat b{display:block;font-family:"Oswald",sans-serif;font-weight:500;font-size:40px;color:var(--orange);line-height:52px}
.stat span{display:block;margin-top:14px;font-size:11px;line-height:17px;color:var(--muted)}

/* about */
.about{top:714px;height:628px}
.about .tagline{left:62px;top:72px;color:var(--teal-text)}
.about h2{position:absolute;left:62px;top:112px;font-size:38px;line-height:44px;font-weight:700;width:490px}
.about-text{position:absolute;left:62px;top:264px;width:420px;font-size:11.5px;line-height:21.5px;color:#444}
.feature{position:absolute;display:flex;gap:12px;align-items:center}
.feature .ico{width:40px;height:40px}
.feature h3{font-size:13px;font-weight:600}
.feature p{font-size:10px;color:var(--muted);margin-top:3px}
.signature{left:62px;top:490px;width:140px;height:36px;background:#ececec;border-radius:4px}
.founder{left:62px;top:535px;font-size:13px;font-weight:700}
.founder span{font-weight:400;color:var(--muted)}
.about .btn{left:286px;top:522px;width:109px;height:34px}
.about .photo-main{left:553px;top:65px;width:279px;height:491px;border-radius:10px;background:linear-gradient(170deg,#d7d5d1,#ece8e2 55%,#b8b1a6)}
.about .photo-group{left:847px;top:65px;width:292px;height:241px;border-radius:10px;background:linear-gradient(160deg,#b9c6cf,#7d8fa0 60%,#5e5147)}
.experience{position:absolute;left:847px;top:327px;width:292px;height:229px;border-radius:10px;background:var(--orange);color:var(--white);text-align:center}
.experience b{display:block;margin-top:60px;font-family:"Montserrat",sans-serif;font-size:62px;font-weight:800;line-height:70px}
.experience span{display:block;margin-top:8px;font-size:17px}

/* services */
.services{top:1342px;height:783px;background:var(--services-bg)}
.services .tagline{left:62px;top:38px;color:var(--ink);font-size:17px}
.services h2{position:absolute;left:104px;top:79px;font-size:38px;line-height:43px;font-weight:700}
.card{position:absolute;width:302px;background:var(--white);border-radius:4px;padding:22px 22px 0}
.card .ico{width:42px;height:42px;border-radius:8px;background:#fbd8b8}
.card h3{margin-top:28px;font-size:15px;font-weight:600}
.card p{margin-top:14px;font-size:10.5px;line-height:18px;color:#777;width:255px}
.card a{display:block;margin-top:14px;font-size:11px;font-weight:600;color:var(--orange);text-decoration:none}

/* team */
.team{top:2125px;height:695px}
.team .tagline{left:62px;top:75px;color:var(--teal-text);font-size:17px}
.team h2{position:absolute;left:62px;top:115px;font-family:"Roboto",sans-serif;font-size:38px;line-height:45px;font-weight:500}
.member{position:absolute;top:236px;width:346px;height:371px}
.member .photo{left:0;top:0;width:346px;height:344px;background:linear-gradient(165deg,#e3e6e8,#b7c6d6 55%,#6f8fb3)}
.member .namebox{position:absolute;left:32px;top:298px;width:280px;height:73px;background:var(--teal);border:4px solid var(--white);border-top:none;padding:10px 20px;color:var(--white)}
.namebox h3{font-size:17px;font-weight:600}
.namebox p{font-size:11px;margin-top:6px}
.namebox .socials{position:absolute;right:18px;top:40px;display:flex;gap:10px}
.namebox .socials i{width:22px;height:22px;border-radius:50%;border:1.5px solid var(--white);display:block}

/* counselor */
.counselor{top:2820px;height:620px}
.counselor h2{position:absolute;left:62px;top:68px;font-size:58px;font-weight:800;color:var(--teal)}
.counselor h3{position:absolute;left:62px;top:145px;width:520px;font-size:26px;line-height:34px;font-weight:500;font-family:"Montserrat",sans-serif}
.counselor-text{position:absolute;left:62px;top:242px;width:560px;font-size:15px;line-height:24px;color:#555}
.point{position:absolute;display:flex;align-items:center;gap:14px;font-size:16px;font-weight:600}
.point svg{width:30px;height:30px}
.counselor .btn{left:62px;top:498px;width:113px;height:34px}
.counselor .teal-block{left:726px;top:44px;width:416px;height:531px;background:var(--teal)}
.counselor .photo{left:687px;top:-7px;width:407px;height:534px;border-radius:130px 0 0 0;background:linear-gradient(165deg,#eceae6,#cfccc5 55%,#3a3a3d)}
.play{position:absolute;left:634px;top:243px;width:112px;height:112px}

/* blog */
.blog{top:3440px;height:679px}
.blog .tagline{left:62px;top:31px;color:var(--teal-text);font-size:17px}
.blog h2{position:absolute;left:62px;top:65px;font-family:"Roboto",sans-serif;font-size:38px;line-height:45px;font-weight:500}
.post{position:absolute;top:203px;width:327px;height:370px}
.post .photo{left:0;top:0;width:327px;height:269px;background:linear-gradient(160deg,#c9d4bf,#e6e2d8 45%,#7f8fa3)}
.post .info{position:absolute;left:7px;top:195px;width:308px;height:134px;background:var(--white);border-radius:6px 6px 0 0;box-shadow:0 4px 14px rgba(0,0,0,.08);padding:20px 24px}
.meta{display:flex;gap:22px;font-size:10px;color:#777;align-items:center}
.meta span{display:flex;align-items:center;gap:6px}
.post h3{margin-top:16px;font-size:15px;line-height:26px;font-weight:400;color:#444}
.post .btn{left:31px;top:329px;width:114px;height:38px}
.dots{position:absolute;left:563px;top:614px;display:flex;gap:6px}
.dots i{width:9px;height:9px;border-radius:50%;border:1px solid var(--orange);display:block}
.dots i:first-child{background:var(--orange)}

/* footer */
.site-footer{top:4119px;height:231px;background:var(--footer);color:var(--white)}
.footer-brand{left:84px;top:36px;font-size:40px;font-weight:400}
.footer-about{position:absolute;left:84px;top:122px;width:440px;font-size:10.5px;line-height:18px;text-transform:uppercase}
.footer-col{position:absolute;top:52px}
.footer-col h4{font-size:17px;font-weight:700;font-family:"Montserrat",sans-serif}
.footer-col ul{list-style:none;margin-top:14px;font-size:13px;line-height:22px}
.footer-col .small{font-size:11px}
.contact-line{display:flex;gap:10px;align-items:center;margin-top:14px;font-size:13px}
.bottom-bar{top:4350px;height:59px;background:var(--orange);color:var(--white)}
.bottom-bar p{position:absolute;left:84px;top:21px;font-size:11px}
.bottom-bar .socials{position:absolute;left:957px;top:16px;display:flex;gap:12px}
.bottom-bar .socials i{width:27px;height:27px;border-radius:50%;border:1.5px solid var(--white);display:block}
</style>
</head>
<body>

<header class="site-header">
  <div class="abs brand">Vela Health</div>
  <nav class="nav">
    <a style="left:515px">Home</a>
    <a style="left:612px">About Us</a>
    <a style="left:727px">Services</a>
    <a style="left:838px">Contact Us</a>
  </nav>
  <div class="btn btn-orange header-cta">Make An Appointment</div>
</header>

<section class="hero">
  <div class="abs cream"></div>
  <div class="abs teal-block"></div>
  <div class="photo" role="img" aria-label="Photo of a therapist talking with a client in a bright room"></div>
  <div class="tagline" style="left:62px;top:68px;color:var(--orange);font-size:14px">
    <svg width="20" height="18" viewBox="0 0 20 18"><path d="M10 17 2 9A4.6 4.6 0 0 1 10 3a4.6 4.6 0 0 1 8 6z" fill="#f37b2a"/></svg>
    A Safe Place
  </div>
  <h1>Private Mental Health Consultation From A Professional</h1>
  <p class="hero-lead">Receive Professional Guidance With Empathy-Driven Solutions To Enhance Mental Health, Foster Resilience, And Create A More Fulfilling Life.</p>
  <div class="btn btn-teal">Make An Appointment ↗</div>
  <div class="btn btn-outline">Learn More ↗</div>
  <div class="stat" style="left:62px"><b>20+</b><span>The Years Of Our<br>Experience</span></div>
  <div class="stat" style="left:185px"><b>840+</b><span>Patients Received<br>Help This Year</span></div>
  <div class="stat" style="left:324px"><b>98%</b><span>Client Improved Their<br>Condition</span></div>
</section>

<section class="about">
  <div class="tagline">
    <svg class="plus" viewBox="0 0 24 24"><rect x="9" y="1" width="6" height="9" fill="#a8dde0"/><rect x="14" y="9" width="9" height="6" fill="#f5a25d"/><rect x="9" y="14" width="6" height="9" fill="#a8dde0"/><rect x="1" y="9" width="9" height="6" fill="#f5a25d"/></svg>
    Welcome To Vela Health Services
  </div>
  <h2>Learn About Our Professional Psychology Thereapy</h2>
  <p class="about-text">Simply Dummy Text Of The Printing And Typesetting Industry. Lorem Ipsum Has Been The Industry's Standard Dummy Text Ever Since The 1500s, When An Unknown Printer Took A Galley Of Type..</p>

  <div class="feature" style="left:62px;top:351px">
    <svg class="ico" viewBox="0 0 40 40"><circle cx="20" cy="20" r="20" fill="#f5a25d"/><path d="M13 20l5 5 9-10" stroke="#fff" stroke-width="3" fill="none"/></svg>
    <div><h3>Qualified Therapies</h3><p>45 Years Of Experience</p></div>
  </div>
  <div class="feature" style="left:288px;top:351px">
    <svg class="ico" viewBox="0 0 40 40"><circle cx="20" cy="20" r="20" fill="#f5a25d"/><path d="M13 20l5 5 9-10" stroke="#fff" stroke-width="3" fill="none"/></svg>
    <div><h3>Individual Counseling</h3><p>Mental Help For Families</p></div>
  </div>
  <div class="feature" style="left:62px;top:427px">
    <svg class="ico" viewBox="0 0 40 40"><circle cx="20" cy="20" r="20" fill="#f5a25d"/><path d="M13 20l5 5 9-10" stroke="#fff" stroke-width="3" fill="none"/></svg>
    <div><h3>Couples Counselling</h3><p>45 Years Of Experience</p></div>
  </div>
  <div class="feature" style="left:288px;top:427px">
    <svg class="ico" viewBox="0 0 40 40"><circle cx="20" cy="20" r="20" fill="#f5a25d"/><path d="M13 20l5 5 9-10" stroke="#fff" stroke-width="3" fill="none"/></svg>
    <div><h3>Referring Therapists</h3><p>Experts You Can Trust</p></div>
  </div>

  <div class="abs signature" role="img" aria-label="Founder's handwritten signature"></div>
  <p class="abs founder">Meera Kapoor- <span>Founder</span></p>
  <div class="btn btn-orange">Learn More</div>

  <div class="photo photo-main" role="img" aria-label="Photo of a psychologist taking notes during a session"></div>
  <div class="photo photo-group" role="img" aria-label="Photo of a group therapy conversation"></div>
  <div class="experience"><b>25+</b><span>Years Of Experience</span></div>
</section>

<section class="services">
  <div class="tagline">
    <svg class="plus" viewBox="0 0 24 24"><rect x="9" y="1" width="6" height="9" fill="#a8dde0"/><rect x="14" y="9" width="9" height="6" fill="#f5a25d"/><rect x="9" y="14" width="6" height="9" fill="#a8dde0"/><rect x="1" y="9" width="9" height="6" fill="#f5a25d"/></svg>
    <span style="margin-left:8px">Our Services</span>
  </div>
  <h2>Professional Support For<br>Mental Wellness.</h2>

  <article class="card" style="left:118px;top:204px;height:243px">
    <div class="ico" role="img" aria-label="Individual therapy icon"></div>
    <h3>Individual Therapy</h3>
    <p>There Are Many Variations Of Passages Of Lorem Ipsum Available, But The Majority TO Suffered Alteration In Some Form,</p>
    <a>Learn More ⟶</a>
  </article>
  <article class="card" style="left:450px;top:207px;height:243px">
    <div class="ico" role="img" aria-label="Depression support icon"></div>
    <h3>Depression Support</h3>
    <p>There Are Many Variations Of Passages Of Lorem Ipsum Available, But The Majority TO Suffered Alteration In Some Form,</p>
    <a>Learn More ⟶</a>
  </article>
  <article class="card" style="left:779px;top:207px;height:243px">
    <div class="ico" role="img" aria-label="Couples counseling icon"></div>
    <h3>Couples Counseling</h3>
    <p>There Are Many Variations Of Passages Of Lorem Ipsum Available, But The Majority TO Suffered Alteration In Some Form,</p>
    <a>Learn More ⟶</a>
  </article>
  <article class="card" style="left:118px;top:473px;height:241px">
    <div class="ico" role="img" aria-label="Family therapy icon"></div>
    <h3>Family Therapy</h3>
    <p>There Are Many Variations Of Passages Of Lorem Ipsum Available, But The Majority TO Suffered Alteration In Some Form,</p>
    <a>Learn More ⟶</a>
  </article>
  <article class="card" style="left:450px;top:476px;height:241px">
    <div class="ico" role="img" aria-label="Life coaching icon"></div>
    <h3>Life Coaching</h3>
    <p>There Are Many Variations Of Passages Of Lorem Ipsum Available, But The Majority TO Suffered Alteration In Some Form,</p>
    <a>Learn More ⟶</a>
  </article>
  <article class="card" style="left:779px;top:476px;height:241px">
    <div class="ico" role="img" aria-label="Stress management icon"></div>
    <h3>Stress Management</h3>
    <p>There Are Many Variations Of Passages Of Lorem Ipsum Available, But The Majority TO Suffered Alteration In Some Form,</p>
    <a>Learn More ⟶</a>
  </article>
</section>

<section class="team">
  <div class="tagline">
    <svg class="plus" viewBox="0 0 24 24"><rect x="9" y="1" width="6" height="9" fill="#a8dde0"/><rect x="14" y="9" width="9" height="6" fill="#f5a25d"/><rect x="9" y="14" width="6" height="9" fill="#a8dde0"/><rect x="1" y="9" width="9" height="6" fill="#f5a25d"/></svg>
    <span style="margin-left:8px">EXPERT MEMBER</span>
  </div>
  <h2>Focusing Your Mind, With The<br>Best Therapeutic Care</h2>

  <div class="member" style="left:60px">
    <div class="photo" role="img" aria-label="Portrait of a senior psychiatrist holding a folder in an office"></div>
    <div class="namebox"><h3>Dr. Laura Bennett</h3><p>Senior Psychiatrist</p><div class="socials"><i></i><i></i><i></i></div></div>
  </div>
  <div class="member" style="left:428px">
    <div class="photo" role="img" aria-label="Portrait of a clinical psychologist seated at a desk"></div>
    <div class="namebox"><h3>Dr. Clara Whitfield</h3><p>Clinical Psychologist</p><div class="socials"><i></i><i></i><i></i></div></div>
  </div>
  <div class="member" style="left:796px">
    <div class="photo" role="img" aria-label="Portrait of a senior psychiatrist in a white coat in a clinic"></div>
    <div class="namebox"><h3>Dr. Owen Hartley</h3><p>Senior Psychiatrist</p><div class="socials"><i></i><i></i><i></i></div></div>
  </div>
</section>

<section class="counselor">
  <div class="abs teal-block"></div>
  <div class="photo" role="img" aria-label="Portrait of a licensed counselor holding a tablet"></div>
  <svg class="play" viewBox="0 0 112 112"><circle cx="56" cy="56" r="56" fill="#a8dde0"/><path d="M48 42v28l22-14z" fill="#fff"/></svg>
  <h2>Dr. Helen Marsh</h2>
  <h3>Licensed Mental Health Counselor, Psychotherapist</h3>
  <p class="counselor-text">There Are Many Variations Of Passages Of Lorem Ipsum Available, But The Majority Have Suffered Alteration In Some Form, By Injected Humour, Or Randomised Words Which Don't Look Even.</p>
  <div class="point" style="left:62px;top:353px"><svg viewBox="0 0 30 30"><circle cx="15" cy="15" r="12" fill="none" stroke="#f5a25d" stroke-width="2.5"/><path d="M9 15l4 4 8-8" stroke="#f5a25d" stroke-width="2.5" fill="none"/></svg>Personal Consultations</div>
  <div class="point" style="left:350px;top:353px"><svg viewBox="0 0 30 30"><circle cx="15" cy="15" r="12" fill="none" stroke="#f5a25d" stroke-width="2.5"/><path d="M9 15l4 4 8-8" stroke="#f5a25d" stroke-width="2.5" fill="none"/></svg>Unique Technique</div>
  <div class="point" style="left:62px;top:399px"><svg viewBox="0 0 30 30"><circle cx="15" cy="15" r="12" fill="none" stroke="#f5a25d" stroke-width="2.5"/><path d="M9 15l4 4 8-8" stroke="#f5a25d" stroke-width="2.5" fill="none"/></svg>Group Therapy</div>
  <div class="point" style="left:350px;top:399px"><svg viewBox="0 0 30 30"><circle cx="15" cy="15" r="12" fill="none" stroke="#f5a25d" stroke-width="2.5"/><path d="M9 15l4 4 8-8" stroke="#f5a25d" stroke-width="2.5" fill="none"/></svg>Couple Problem</div>
  <div class="point" style="left:62px;top:443px"><svg viewBox="0 0 30 30"><circle cx="15" cy="15" r="12" fill="none" stroke="#f5a25d" stroke-width="2.5"/><path d="M9 15l4 4 8-8" stroke="#f5a25d" stroke-width="2.5" fill="none"/></svg>Online Therapy</div>
  <div class="btn btn-orange">Learn More</div>
</section>

<section class="blog">
  <div class="tagline">
    <svg class="plus" viewBox="0 0 24 24"><rect x="9" y="1" width="6" height="9" fill="#a8dde0"/><rect x="14" y="9" width="9" height="6" fill="#f5a25d"/><rect x="9" y="14" width="6" height="9" fill="#a8dde0"/><rect x="1" y="9" width="9" height="6" fill="#f5a25d"/></svg>
    <span style="margin-left:8px">Our Blog</span>
  </div>
  <h2>Explore Mental Health<br>New Insights Today.</h2>

  <article class="post" style="left:84px">
    <div class="photo" role="img" aria-label="Photo of a counseling session between two women"></div>
    <div class="info">
      <div class="meta"><span><svg width="12" height="12" viewBox="0 0 12 12"><circle cx="6" cy="4" r="3" fill="none" stroke="#888"/><path d="M1 12a5 5 0 0 1 10 0" fill="none" stroke="#888"/></svg>By Admin</span><span><svg width="12" height="12" viewBox="0 0 12 12"><rect x="1" y="2" width="10" height="9" fill="none" stroke="#888"/><path d="M1 5h10" stroke="#888"/></svg>March 21, 2017</span></div>
      <h3>The Power Of Mindfulness For Stress Management</h3>
    </div>
    <div class="btn btn-orange">Read More</div>
  </article>
  <article class="post" style="left:437px;top:206px">
    <div class="photo" role="img" aria-label="Photo of a woman in a psychotherapy session"></div>
    <div class="info">
      <div class="meta"><span><svg width="12" height="12" viewBox="0 0 12 12"><circle cx="6" cy="4" r="3" fill="none" stroke="#888"/><path d="M1 12a5 5 0 0 1 10 0" fill="none" stroke="#888"/></svg>By Admin</span><span><svg width="12" height="12" viewBox="0 0 12 12"><rect x="1" y="2" width="10" height="9" fill="none" stroke="#888"/><path d="M1 5h10" stroke="#888"/></svg>March 21, 2017</span></div>
      <h3>The Pros And Cons Of Group Psychotherapy</h3>
    </div>
    <div class="btn btn-orange">Read More</div>
  </article>
  <article class="post" style="left:789px;top:205px">
    <div class="photo" role="img" aria-label="Photo of two women talking in a bright office"></div>
    <div class="info">
      <div class="meta"><span><svg width="12" height="12" viewBox="0 0 12 12"><circle cx="6" cy="4" r="3" fill="none" stroke="#888"/><path d="M1 12a5 5 0 0 1 10 0" fill="none" stroke="#888"/></svg>By Admin</span><span><svg width="12" height="12" viewBox="0 0 12 12"><rect x="1" y="2" width="10" height="9" fill="none" stroke="#888"/><path d="M1 5h10" stroke="#888"/></svg>March 21, 2017</span></div>
      <h3>The Power Of Mindfulness For Stress Management</h3>
    </div>
    <div class="btn btn-orange">Read More</div>
  </article>
  <div class="dots"><i></i><i></i><i></i><i></i><i></i></div>
</section>

<footer class="site-footer">
  <div class="abs footer-brand">Vela Health</div>
  <p class="footer-about">Long established fact that a reader will be distracted by the readable content of a page when looking at its layout. The point of using Lorem Ipsum is that it has a more-or-less normal distribution</p>
  <div class="footer-col" style="left:583px">
    <h4>QUICK LINKS</h4>
    <ul><li>› Home</li><li>› About Us</li><li>› Services</li><li class="small">› CONTACT US</li></ul>
  </div>
  <div class="footer-col" style="left:813px">
    <h4>CONTACT INFO</h4>
    <div class="contact-line" style="margin-top:20px"><svg width="16" height="12" viewBox="0 0 16 12"><rect x=".5" y=".5" width="15" height="11" fill="none" stroke="#fff"/><path d="M.5.5 8 7 15.5.5" fill="none" stroke="#fff"/></svg>Email - hello@velahealth.example</div>
    <div class="contact-line"><svg width="14" height="14" viewBox="0 0 14 14"><path d="M3 1l3 3-2 2a8 8 0 0 0 4 4l2-2 3 3-2 2C6 13 1 8 1 3z" fill="none" stroke="#fff"/></svg>Phone - (202) 555-0148</div>
  </div>
</footer>
<div class="abs bottom-bar" style="left:0;width:1200px">
  <p>© 2025 Info Vela Health Services. All Rights Reserved</p>
  <div class="socials"><i></i><i></i><i></i><i></i></div>
</div>

</body>
</html>
```